HomeBridle business card and stationary design

We are looking for a simple yet elegant design for our mortgage company business card and stationary.

The card should include:
Name (Derek Walsh)
Title (CEO)
Phone Number (614-208-3917)
Address (48 Birchfield Court, Suite 314, Marlow, OH 43952)
Email (email@homebridle-example.com)
"NMLS" i.e. (NMLS 61947)
"Company NMLS" (Company NMLS 472815)

See above

```html
<!DOCTYPE html>
<html lang="en">
<head>
<meta charset="utf-8">
<title>HomeBridle Business Card</title>
<link href="https://fonts.googleapis.com/css2?family=Montserrat:wght@500;600;700&display=swap" rel="stylesheet">
<style>
  :root {
    --page: #6b6b6d;
    --navy: #1b2634;
    --navy-light: #2c3a49;
    --sky: #29abe2;
    --ink: #141c26;
    --paper: #ffffff;
  }
  * { margin: 0; padding: 0; box-sizing: border-box; }
  html, body {
    width: 1200px; height: 900px; overflow: hidden;
    background: var(--page);
    font-family: 'Montserrat', Arial, sans-serif;
  }
  .card {
    position: absolute;
    left: 280px;
    width: 640px; height: 366px;
    overflow: hidden;
    box-shadow: 0 10px 24px rgba(0,0,0,.35);
  }
  .card-front {
    top: 56px;
    background: linear-gradient(120deg, var(--navy) 45%, var(--navy-light) 100%);
  }
  .card-back {
    top: 478px;
    background: var(--paper);
  }
  .wordmark {
    font-weight: 600;
    letter-spacing: 1px;
    white-space: nowrap;
  }
  .card-front .wordmark {
    position: absolute; left: 0; right: 0; top: 120px;
    text-align: center;
    font-size: 62px;
    color: var(--paper);
  }
  .front-url {
    position: absolute; left: 0; right: 0; bottom: 34px;
    text-align: center;
    font-size: 15px; font-weight: 600; letter-spacing: 1.5px;
    color: var(--sky);
  }
  .card-back .wordmark {
    position: absolute; left: 36px; top: 110px;
    font-size: 44px;
    color: var(--ink);
  }
  .details {
    position: absolute; left: 372px; top: 36px;
    color: var(--ink);
    font-size: 13px; font-weight: 500; letter-spacing: .8px;
    line-height: 1.5;
  }
  .person-name {
    font-size: 24px; font-weight: 700; letter-spacing: .5px; line-height: 1.1;
  }
  .person-name .surname { color: var(--sky); }
  .person-title {
    color: var(--sky); font-weight: 600; font-size: 13px; letter-spacing: 1.5px;
    margin-bottom: 4px;
  }
  .address { margin-top: 20px; margin-bottom: 8px; }
  .contact-line { display: flex; align-items: center; gap: 9px; }
  .contact-line svg { width: 13px; height: 13px; flex: none; }
  .band { position: absolute; left: 0; bottom: 0; width: 640px; height: 30px; }
</style>
</head>
<body>
  <section class="card card-front">
    <div class="wordmark">HomeBridle</div>
    <div class="front-url">www.homebridle.com</div>
  </section>

  <section class="card card-back">
    <div class="wordmark">HomeBridle</div>

    <div class="details">
      <div class="person-name">Derek <span class="surname">Walsh</span></div>
      <div class="person-title">CEO</div>
      <div>NMLS 61947</div>
      <div>Company NMLS 472815</div>
      <div class="address">48 Birchfield Court, Suite 314,<br>Marlow, OH 43952</div>
      <div class="contact-line">
        <svg viewBox="0 0 24 24"><path fill="#29abe2" d="M6.6 10.8a15.1 15.1 0 0 0 6.6 6.6l2.2-2.2c.3-.3.7-.4 1-.2 1.1.4 2.3.6 3.6.6.6 0 1 .4 1 1V20c0 .6-.4 1-1 1A17 17 0 0 1 3 4c0-.6.4-1 1-1h3.5c.6 0 1 .4 1 1 0 1.3.2 2.5.6 3.6.1.3 0 .7-.2 1z"/></svg>
        <span>614-208-3917</span>
      </div>
      <div class="contact-line">
        <svg viewBox="0 0 24 24"><rect x="2" y="5" width="20" height="14" rx="1.5" fill="#29abe2"/><path d="M2.5 6l9.5 7 9.5-7" fill="none" stroke="#fff" stroke-width="1.8"/></svg>
        <span>email@homebridle-example.com</span>
      </div>
      <div class="contact-line">
        <svg viewBox="0 0 24 24"><circle cx="12" cy="12" r="10" fill="#29abe2"/><path d="M2 12h20M12 2c3 3 3 17 0 20M12 2c-3 3-3 17 0 20" fill="none" stroke="#fff" stroke-width="1.4"/></svg>
        <span>www.homebridle.com</span>
      </div>
    </div>

    <svg class="band" viewBox="0 0 640 30" preserveAspectRatio="none">
      <polygon points="0,16 354,16 346,30 0,30" fill="#1b2634"/>
      <polygon points="364,8 640,8 640,30 352,30" fill="#29abe2"/>
    </svg>
  </section>
</body>
</html>
```